Car Accessories Distributor Needs a Logo Re-design

We are Lindo Car Depot Pte Ltd, a distributor in Singapore importing car accessories from countries such as Taiwan and China and selling it to local car workshops and accessories shops.
"Voro" is means 'gold' in a Chinese dialect and it also signifies prosperity to Chinese businessmen. Therefore we would like to have the colour gold retained in the design. We hope to get a minimalist and/or creative logo to show a brand new look of the company and perhaps incorporate an impression related to cars. For the company's name, a modern font would be refreshing as well.
Please browse and take a look at our current website www.vorocardepot-example.com to understand what we do and what products we carry. Our current logo is there for your perusal as well.
Updates
Updated with some sample logos which are minimalist and creative.
Reason: Polling amongst colleagues and managers.
Thank you for your submissions! We will be making our choice as soon as possible!
Target Market(s)
Car workshops & car accessories shops in Singapore
Suppliers based in China & Taiwan
Occasional walk-in customers who enquire about products (unimportant at the moment)
Industry/Entity Type
It Company
Logo Text
VORO
Font styles to use
Requirements
Must have
- For name card, chinese name is required:
宇汽车用品私人有限公司
Address, contact, fax and website would need to be there too.

```html
<!DOCTYPE html>
<html lang="en">
<head>
<meta charset="utf-8">
<title>Lindo Car Depot Pte Ltd – Business Card &amp; Logo</title>
<link rel="stylesheet" href="https://fonts.googleapis.com/css2?family=Questrial&family=Noto+Sans+SC:wght@300&display=swap">
<style>
  :root {
    --stage: #3b3734;
    --card: #0b0b0b;
    --gold: #d9a51c;
    --gold-light: #f2c83a;
    --white: #f4f4f4;
    --ink: #222;
    --paper: #ffffff;
  }
  * { margin: 0; padding: 0; box-sizing: border-box; }
  html, body { width: 1200px; height: 1000px; overflow: hidden; }
  body { background: var(--paper); font-family: "Questrial", sans-serif; position: relative; }

  .stage { position: absolute; left: 0; top: 0; width: 1200px; height: 855px; background: var(--stage); }

  .card { position: absolute; top: 270px; width: 500px; height: 290px; background: var(--card);
          box-shadow: 0 14px 30px rgba(0,0,0,.45); overflow: hidden; color: var(--white); }
  .card--front { left: 70px; }
  .card--back { left: 630px; }

  .brand-mark { position: absolute; color: var(--gold); font-family: "Questrial", sans-serif; line-height: 1; letter-spacing: 2px; }

  .card--front .brand-mark { left: 34px; top: 30px; font-size: 92px; }
  .card--front .company { position: absolute; left: 28px; top: 128px; font-size: 22px; letter-spacing: .5px;
                          padding-bottom: 6px; border-bottom: 1px solid rgba(255,255,255,.25); }
  .gold-bar { position: absolute; height: 6px; background: linear-gradient(90deg, var(--gold), var(--gold-light)); }
  .gold-bar--left { left: 0; top: 182px; width: 150px; }
  .gold-bar--right { left: 300px; top: 214px; width: 200px; }
  .website { position: absolute; left: 162px; top: 196px; font-size: 11px; color: var(--white); }

  .card--back .company { position: absolute; left: 180px; top: 34px; font-size: 21px; }
  .card--back .company-cn { position: absolute; left: 180px; top: 66px; font-family: "Noto Sans SC", sans-serif;
                            font-size: 12px; color: var(--gold); letter-spacing: 1px; }
  .card--back .brand-mark { right: 20px; top: 96px; font-size: 38px; }
  .address { position: absolute; left: 24px; top: 148px; font-size: 13px; line-height: 17px; }
  .address-title { color: var(--gold); font-size: 17px; margin-bottom: 2px; }
  .contact { position: absolute; right: 22px; bottom: 20px; text-align: right; font-size: 15px; line-height: 21px; }
  .contact-name { color: var(--gold); font-size: 19px; margin-bottom: 4px; }
  .contact-line { display: flex; justify-content: flex-end; align-items: center; gap: 6px; }
  .contact-line svg { width: 12px; height: 12px; fill: none; stroke: var(--gold); stroke-width: 1.3; }

  .lockup { position: absolute; top: 872px; width: 260px; text-align: left; }
  .lockup--left { left: 30px; }
  .lockup--right { left: 912px; }
  .lockup .brand-mark { position: static; font-size: 62px; display: block; }
  .lockup-rule { height: 2px; margin: 4px 0 5px; background: linear-gradient(90deg, var(--gold), rgba(217,165,28,.15)); }
  .lockup-name { font-size: 18px; color: var(--ink); letter-spacing: .5px; }
</style>
</head>
<body>
  <section class="stage">
    <article class="card card--front">
      <div class="brand-mark">VORO</div>
      <div class="company">Lindo Car Depot Pte Ltd</div>
      <div class="gold-bar gold-bar--left"></div>
      <div class="website">www.vorocardepot-example.com</div>
      <div class="gold-bar gold-bar--right"></div>
    </article>

    <article class="card card--back">
      <div class="company">Lindo Car Depot Pte Ltd</div>
      <div class="company-cn">宇汽车用品私人有限公司</div>
      <div class="brand-mark">VORO</div>
      <div class="address">
        <div class="address-title">Address</div>
        <div>voro auto</div>
        <div>voro auto voro auto</div>
        <div>voro auto voro auto</div>
      </div>
      <div class="contact">
        <div class="contact-name">Your Name here</div>
        <div class="contact-line">1234567890
          <svg viewBox="0 0 12 12"><rect x="3" y="1" width="6" height="10" rx="1"/><line x1="5" y1="9" x2="7" y2="9"/></svg>
        </div>
        <div class="contact-line">1234567890
          <svg viewBox="0 0 12 12"><rect x="1.5" y="5" width="9" height="6" rx="1"/><path d="M2 5 V3 H10 V5"/><line x1="4" y1="8" x2="8" y2="8"/></svg>
        </div>
        <div class="contact-line">sales@vorocardepot-example.com
          <svg viewBox="0 0 12 12"><rect x="1" y="2.5" width="10" height="7"/><path d="M1 2.5 L6 7 L11 2.5"/></svg>
        </div>
      </div>
    </article>
  </section>

  <div class="lockup lockup--left">
    <span class="brand-mark">VORO</span>
    <div class="lockup-rule"></div>
    <div class="lockup-name">Lindo Car Depot Pte Ltd</div>
  </div>
  <div class="lockup lockup--right">
    <span class="brand-mark">VORO</span>
    <div class="lockup-rule"></div>
    <div class="lockup-name">Lindo Car Depot Pte Ltd</div>
  </div>
</body>
</html>
```